Business Card Design Project

We are looking to redesign the logo, business card and stationary of one of our group companies - KESTRAL SUPPLY COMPANY LLC.

The company specialises in industrial PVC and CPVC Piping systems. It is situated in the Middle East and the focus is purely in this region.

The logo work is already completed. The file is uploaded for the reference.

We are looking for a clean minimalistic design for the business card.

regards
Ormund
Updates

Hello Everyone!

Thanks for submitting your designs. 

Yet to find the right design. Probably the below links will give you guys some more idea on what we would like.

Minimalist design with some creativity.

Ormund

http://plaincardgallery.example/inspiration/15-beautifully-minimal-business-cards

http://www.quietlayouthub.example/2011/11/14/30-minimalist-business-card-design/

http://www.firmpixelnotes.example/inspiration/minimal-business-cards/

Target Market(s)

Industrial users

Industry/Entity Type

Industrial

Requirements
Must have
• - Minimalistic design

- Back side of the card should include the manufacturer BRAVOLINE CANADA's decal. The file is upload for the reference

- Further information
Company Name:
KESTRAL SUPPLY COMPANY LLC
Address:
PO Box 9087, Sharjah Industrial Area 5, Qutrani Road
Sharjah, United Arab Emirates
Telephone:
+971-6-5018-392
Fax:
+977-6-5018-393
Email:
mail@ksc-holding.example

- FYI, Kestral Supply Company LLC is the authorised distributor for BRAVOLINE CANADA in the UAE. For further information on bravoline please visit the website www.bravoline.example

```html
<!DOCTYPE html>
<html lang="en">
<head>
<meta charset="utf-8">
<title>Kestral Supply Company LLC – Business Card</title>
<link rel="stylesheet" href="https://fonts.googleapis.com/css2?family=Arimo:wght@400;700&display=swap">
<style>
  :root {
    --page: #ffffff;
    --blue-deep: #1846e6;
    --blue-mid: #3f74f0;
    --blue-light: #8ed6fb;
    --ink: #0c0c14;
    --white: #ffffff;
    --stripe: rgba(255, 255, 255, 0.10);
    --mark: #0f2a8a;
  }
  * { box-sizing: border-box; margin: 0; padding: 0; }
  html, body {
    width: 1200px; height: 900px; overflow: hidden;
    background: var(--page);
    font-family: "Arimo", Arial, sans-serif;
  }
  .canvas { position: relative; width: 1200px; height: 900px; }

  .card {
    position: absolute;
    width: 576px; height: 352px;
    overflow: hidden;
  }
  .card-front { background: linear-gradient(90deg, var(--blue-deep) 0%, var(--blue-mid) 35%, var(--blue-light) 100%); }
  .card-back { background: linear-gradient(90deg, var(--blue-deep) 0%, var(--blue-mid) 60%, var(--blue-light) 100%); }

  .card--large-front { left: 16px; top: 32px; }
  .card--large-back { left: 608px; top: 220px; }
  .card--small-back { left: 226px; top: 645px; transform: scale(0.585, 0.58); transform-origin: 0 0; }
  .card--small-front { left: 573px; top: 645px; transform: scale(0.585, 0.58); transform-origin: 0 0; }

  /* front */
  .brand-mark {
    position: absolute; left: 112px; top: 114px;
    width: 40px; height: 40px;
    background: var(--mark);
  }
  .company-name {
    position: absolute; left: 168px; top: 125px;
    font-size: 21px; font-weight: 700; color: var(--white);
    letter-spacing: 0.2px; white-space: nowrap;
  }
  .contact {
    position: absolute; left: 0; right: 0; top: 276px;
    text-align: center; color: var(--white);
    font-size: 14px; line-height: 22px; font-style: normal;
  }
  .contact .gap { display: inline-block; width: 22px; }

  /* back */
  .stripes { position: absolute; left: 0; right: 0; top: 102px; }
  .stripes span {
    display: block; height: 20px; margin-bottom: 5.5px;
    background: var(--stripe);
  }
  .services { position: absolute; left: 155px; top: 104px; }
  .services-title { font-size: 15px; font-weight: 700; color: var(--ink); line-height: 17px; margin-bottom: 10px; }
  .services-list {
    list-style: none;
    display: grid; grid-template-columns: 139px auto;
    row-gap: 8.5px; line-height: 17px;
    color: var(--white); font-size: 14px; letter-spacing: 0.3px;
  }
  .partner { position: absolute; left: 215px; top: 279px; width: 200px; height: 42px; }
  .partner-mark { position: absolute; left: 0; top: 0; width: 40px; height: 40px; background: var(--mark); }
  .partner-name { position: absolute; left: 51px; top: 6px; font-size: 17px; color: var(--ink); white-space: nowrap; }
  .partner-tag { position: absolute; right: 0; top: 27px; font-size: 12px; color: var(--ink); white-space: nowrap; }
</style>
</head>
<body>
<main class="canvas">

  <section class="card card-front card--large-front" aria-label="Card front">
    <div class="brand-mark"></div>
    <h1 class="company-name">KESTRAL SUPPLY COMPANY LLC</h1>
    <address class="contact">
      PO Box 9087, Sharjah Industrial Area 5, Qutrani Road Sharjah, United Arab Emirates<br>
      Tel: +971-6-5018-392<span class="gap"></span>Fax: +977-6-5018-393<br>
      Email: mail@ksc-holding.example
    </address>
  </section>

  <section class="card card-back card--large-back" aria-label="Card back">
    <div class="stripes"><span></span><span></span><span></span><span></span><span></span><span></span><span></span><span></span></div>
    <div class="services">
      <h2 class="services-title">COMMUNITY</h2>
      <ul class="services-list">
        <li>PIPES</li><li>DESIGN</li>
        <li>FITTINGS</li><li>LOGISTICS</li>
        <li>VALVES</li><li>FINANCE</li>
        <li>ACCESSORIES</li><li>SOFTWARE</li>
        <li>ENGINEERING</li><li>INFRASTRUCURE</li>
      </ul>
    </div>
    <div class="partner">
      <div class="partner-mark"></div>
      <p class="partner-name">Bravoline Canada</p>
      <p class="partner-tag">re-engineering</p>
    </div>
  </section>

  <section class="card card-back card--small-back" aria-label="Card back, preview">
    <div class="stripes"><span></span><span></span><span></span><span></span><span></span><span></span><span></span><span></span></div>
    <div class="services">
      <h2 class="services-title">COMMUNITY</h2>
      <ul class="services-list">
        <li>PIPES</li><li>DESIGN</li>
        <li>FITTINGS</li><li>LOGISTICS</li>
        <li>VALVES</li><li>FINANCE</li>
        <li>ACCESSORIES</li><li>SOFTWARE</li>
        <li>ENGINEERING</li><li>INFRASTRUCURE</li>
      </ul>
    </div>
    <div class="partner">
      <div class="partner-mark"></div>
      <p class="partner-name">Bravoline Canada</p>
      <p class="partner-tag">re-engineering</p>
    </div>
  </section>

  <section class="card card-front card--small-front" aria-label="Card front, preview">
    <div class="brand-mark"></div>
    <p class="company-name">KESTRAL SUPPLY COMPANY LLC</p>
    <address class="contact">
      PO Box 9087, Sharjah Industrial Area 5, Qutrani Road Sharjah, United Arab Emirates<br>
      Tel: +971-6-5018-392<span class="gap"></span>Fax: +977-6-5018-393<br>
      Email: mail@ksc-holding.example
    </address>
  </section>

</main>
</body>
</html>
```